Business Card Design for Event Planning Company

Create a business card for event planning company using our new logo. After I pick the design, I will need files made for 6 employees. Our company provides event design & logistics services as well as venue management. The font should be sans serif and complementary to the logo. I will need to know the name of the font selected for the final design. The phone numbers listed should be separated by "." not "-"

Address for the card
PO Box 318, Washington, DC 20019

Card One
Lorna Pettibone
lpettibone@galavoyant.com
202.481.7730

Card Two
Miriam Okonkwo
mokonkwo@galavoyant.com
202.556.2047

Card Three
Tessa Varnholt
tvarnholt@galavoyant.com
978.620.4471

Card Four
Robin Fess
rfess@galavoyant.com
202.718.3362

Card Five
Ada-Rose Pelletan-Uzor
adarose@galavoyant.com
202.839.1205

Card Six
Beatrix Holloway
Beatrix@galavoyant.com
202.492.6618

Target Market(s)

Corporate/Non-Profit

Industry/Entity Type

Event Planning

Contact Information for Business Card

Address for the card

Card One
Lorna Pettibone
lpettibone@galavoyant.com
202.481.7730

Card Two
Miriam Okonkwo
202.556.2047

Card Three
Tessa Varnholt
978.620.4471

Card Four
Robin Fess
rfess@galavoyant.com
202.718.3362

Card Five
Ada-Rose Pelletan-Uzor
202.839.1205

Card Six
Beatrix Holloway
202.492.6618

Font styles to use
Sans Serif

Colors

Designer to choose colors to be used in the design.

Requirements
Must have
• Two-sided with logo
Should not have
• Extra colors or be too busy

```html
<!DOCTYPE html>
<html lang="en">
<head>
<meta charset="utf-8">
<title>Galavoyant business card</title>
<link rel="stylesheet" href="https://fonts.googleapis.com/css2?family=Work+Sans:wght@300;400;700&display=swap">
<style>
  :root {
    --stage: #e9e7e4;
    --card: #1c1c1d;
    --card-deep: #141415;
    --white: #ffffff;
    --teal: #5ba3a5;
    --muted: #d8d8d8;
  }
  * { margin: 0; padding: 0; box-sizing: border-box; }
  html, body { width: 1200px; height: 715px; overflow: hidden; }
  body {
    background: var(--stage);
    font-family: "Work Sans", Arial, sans-serif;
    position: relative;
  }
  .card {
    position: absolute;
    width: 540px;
    height: 309px;
    background: var(--card);
    overflow: hidden;
    box-shadow: 0 10px 28px rgba(0,0,0,0.22);
  }
  /* Back side */
  .card-back { left: 40px; top: 70px; }
  .pattern-fill {
    position: absolute; inset: 0;
    background: radial-gradient(ellipse at 50% 45%, #2b2b2d 0%, var(--card) 60%, var(--card-deep) 100%);
  }
  .back-wordmark {
    position: absolute; left: 0; right: 0; top: 50%;
    transform: translateY(-50%);
    text-align: center;
    font-weight: 300;
    font-size: 54px;
    letter-spacing: 1px;
    color: var(--white);
  }
  /* Front side */
  .card-front { left: 620px; top: 330px; }
  .brand {
    position: absolute; right: 30px; top: 44px;
    display: flex; align-items: center; gap: 12px;
  }
  .brand-name {
    font-weight: 300; font-size: 38px; color: var(--white); letter-spacing: 0.5px;
  }
  .brand-dot {
    width: 26px; height: 26px; border-radius: 50%; background: var(--teal);
  }
  .person-name {
    position: absolute; left: 30px; top: 118px;
    font-weight: 700; font-size: 17px; letter-spacing: 0.5px;
    text-transform: uppercase; color: var(--white);
  }
  .person-name .surname { color: var(--teal); }
  .divider {
    position: absolute; left: 30px; right: 30px; top: 148px;
    height: 1px; background: var(--white);
  }
  .contact-list {
    position: absolute; left: 30px; top: 160px;
    list-style: none; font-size: 13px; color: var(--white);
  }
  .contact-list li { display: flex; align-items: center; gap: 9px; height: 22px; }
  .contact-list svg { width: 11px; height: 11px; flex: none; }
  .address {
    position: absolute; right: 30px; top: 205px;
    text-align: right; font-size: 13px; line-height: 1.5; color: var(--white);
  }
  .band {
    position: absolute; left: 0; right: 0; bottom: 0; height: 34px;
    background: var(--teal);
  }
</style>
</head>
<body>
  <section class="card card-back" aria-label="Card back">
    <div class="pattern-fill" role="img" aria-label="Faint tone-on-tone repeating monogram pattern across the card"></div>
    <div class="back-wordmark">galavoyant</div>
  </section>

  <section class="card card-front" aria-label="Card front">
    <div class="brand">
      <span class="brand-dot"></span>
      <span class="brand-name">galavoyant</span>
    </div>
    <h1 class="person-name">Lorna <span class="surname">Pettibone</span></h1>
    <div class="divider"></div>
    <ul class="contact-list">
      <li>
        <svg viewBox="0 0 12 12" aria-hidden="true"><path d="M3 1 L5 3.5 L4 5 Q5 7 7 8 L8.5 7 L11 9 L9.5 11 Q4 10.5 1 3 Z" fill="none" stroke="#5ba3a5" stroke-width="1.1" stroke-linejoin="round"/></svg>
        <span>202.481.7730</span>
      </li>
      <li>
        <svg viewBox="0 0 12 12" aria-hidden="true"><rect x="1" y="2.5" width="10" height="7" fill="none" stroke="#5ba3a5" stroke-width="1.1"/><path d="M1 2.5 L6 6.5 L11 2.5" fill="none" stroke="#5ba3a5" stroke-width="1.1"/></svg>
        <span>lpettibone@galavoyant.com</span>
      </li>
    </ul>
    <address class="address" style="font-style:normal">PO Box 318,<br>Washington, DC 20019</address>
    <div class="band"></div>
  </section>
</body>
</html>
```